Corrigan Architecture (business card)

We need a business card design. We are a full service architectural firm that specializes in mostly residential projects and some commercial projects. We are located in Hudson Valley, New York. We work with high end clients and want a business card that is memorable and has a sleek, modern, design but will not go out of style (timeless).

Target Market(s)

high end residential clients

Industry/Entity Type

Architect

Contact Information for Business Card

Front of card
Company Logo
website: www.corriganarchitectur.example
what we do: residential, Commercial

back of card
Owner's Name: Dorian Corrigan
owner's title: Principal
Business address: 2873 Route 92 Suite A, Brellfordton, NY 12688
phone number: 845-608-2917
e-mail: dc@corriganarchitecture.example

We like:
icons
sleek and clean design
simple not too busy or too much text

Font styles to use
Sans Serif

Colors
0356a4

Requirements
Must have
• company colors are navy blue, white, and gray
• Front of card
• Company Logo
• website: www.corriganarchitectur.example
• what we do: residential, Commercial
• back of card
• Owner's Name: Dorian Corrigan
• owner's title: Principal
• Business address: 2873 Route 92 Suite A, Brellfordton, NY 12688
• phone number: 845-608-2917
• e-mail: dc@corriganarchitecture.example
Nice to have
• We like:
• icons
• sleek and clean design
• simple not too much text
• color of the card to be either blue or gray
Should not have
• we do not like houses in the design or plans of houses-this is over done and we don't like it.
• no QR CODES

```html
<!DOCTYPE html>
<html lang="en">
<head>
<meta charset="utf-8">
<title>Corrigan Architecture – Business Card</title>
<link rel="stylesheet" href="https://fonts.googleapis.com/css2?family=Jost:wght@300;400&family=Roboto:wght@400;500&display=swap">
<style>
  :root {
    --navy: #1f236e;
    --navy-deep: #1a1e62;
    --silver: #c9c9cb;
    --grey-text: #8a8a8c;
    --grey-band: #8e8e8e;
    --paper-light: #ececec;
    --paper-mid: #d8d8d9;
    --backdrop: #f2f2f2;
    --white: #ffffff;
  }
  * { box-sizing: border-box; margin: 0; padding: 0; }
  html, body { width: 1200px; height: 576px; overflow: hidden; }
  body { background: var(--backdrop); position: relative; }

  .card {
    position: absolute;
    top: 138px;
    width: 484px;
    height: 294px;
    border-radius: 12px;
    overflow: hidden;
  }

  /* Front */
  .card-front {
    left: 82px;
    background: var(--navy);
    font-family: "Jost", sans-serif;
    color: var(--silver);
  }
  .front-brand {
    position: absolute;
    left: 0; right: 0;
    top: 100px;
    text-align: center;
    font-weight: 300;
    font-size: 31px;
    letter-spacing: 0.5px;
    color: var(--silver);
    text-transform: uppercase;
  }
  .front-services {
    position: absolute;
    left: 0; right: 0;
    top: 162px;
    text-align: center;
    font-weight: 300;
    font-size: 13px;
    letter-spacing: 0.3px;
    color: var(--white);
    text-transform: uppercase;
  }
  .front-services .divider { margin: 0 9px; }
  .front-web {
    position: absolute;
    left: 0; right: 0;
    top: 256px;
    text-align: center;
    font-weight: 300;
    font-size: 13px;
    color: var(--white);
    letter-spacing: 0.3px;
  }

  /* Back */
  .card-back {
    left: 602px;
    background: linear-gradient(135deg, var(--paper-light) 0%, var(--paper-mid) 100%);
    font-family: "Roboto", sans-serif;
  }
  .back-tab {
    position: absolute;
    left: -25px;
    top: 44px;
    width: 34px;
    height: 50px;
    border-radius: 50%;
    background: var(--navy);
  }
  .owner-name {
    position: absolute;
    left: 24px;
    top: 52px;
    font-weight: 500;
    font-size: 18px;
    color: var(--navy);
  }
  .owner-title {
    position: absolute;
    left: 24px;
    top: 77px;
    font-size: 12px;
    color: var(--grey-text);
  }
  .back-brand {
    position: absolute;
    right: 22px;
    top: 118px;
    text-align: right;
    font-family: "Jost", sans-serif;
    font-weight: 300;
    font-size: 22px;
    line-height: 1.2;
    color: var(--grey-text);
    text-transform: uppercase;
  }
  .contact-list {
    position: absolute;
    left: 27px;
    top: 202px;
    list-style: none;
  }
  .contact-item {
    display: flex;
    align-items: center;
    height: 18px;
    font-size: 12.5px;
    color: var(--navy);
  }
  .contact-icon { width: 12px; height: 12px; margin-right: 10px; flex: none; }
  .address {
    position: absolute;
    right: 22px;
    top: 206px;
    text-align: right;
    font-size: 12.5px;
    line-height: 19px;
    color: var(--navy);
  }
  .back-bands { position: absolute; left: 0; top: 0; }
  .back-services {
    position: absolute;
    right: 22px;
    top: 264px;
    font-size: 12.5px;
    color: var(--white);
  }
  .back-services .divider { margin: 0 6px; }
</style>
</head>
<body>

<section class="card card-front">
  <div class="front-brand">Corrigan Architecture</div>
  <div class="front-services">Residential<span class="divider">|</span>Commercial</div>
  <div class="front-web">www.corriganarchitectur.example</div>
</section>

<section class="card card-back">
  <div class="back-tab"></div>
  <svg class="back-bands" width="484" height="294" viewBox="0 0 484 294">
    <rect x="0" y="279" width="236" height="15" fill="var(--grey-band)"/>
    <polygon points="246,255 484,255 484,294 222,294" fill="var(--navy)"/>
  </svg>

  <div class="owner-name">Dorian Corrigan</div>
  <div class="owner-title">Principal/Owner</div>

  <div class="back-brand">Corrigan<br>Architecture</div>

  <ul class="contact-list">
    <li class="contact-item">
      <svg class="contact-icon" viewBox="0 0 12 12"><path d="M1 3.5C1 2.5 2.5 1.5 6 1.5S11 2.5 11 3.5V5H8.5V4H3.5V5H1Z M3 5.5H9L10.5 10.5H1.5Z" fill="var(--grey-text)"/></svg>
      845-608-2917
    </li>
    <li class="contact-item">
      <svg class="contact-icon" viewBox="0 0 12 12"><rect x="1" y="2.5" width="10" height="7" fill="var(--grey-text)"/><path d="M1 2.5L6 6.5L11 2.5" stroke="var(--paper-light)" stroke-width="1" fill="none"/></svg>
      dc@corriganarchitecture.example
    </li>
    <li class="contact-item">
      <svg class="contact-icon" viewBox="0 0 12 12"><circle cx="6" cy="6" r="4.8" fill="none" stroke="var(--grey-text)" stroke-width="1"/><ellipse cx="6" cy="6" rx="2" ry="4.8" fill="none" stroke="var(--grey-text)" stroke-width="0.8"/><line x1="1.2" y1="6" x2="10.8" y2="6" stroke="var(--grey-text)" stroke-width="0.8"/></svg>
      www.corriganarchitectur.example
    </li>
  </ul>

  <div class="address">2873 Route 92 Suite A<br>Brellfordton, NY 12688</div>

  <div class="back-services">Residential<span class="divider">|</span>Commercial</div>
</section>

</body>
</html>
```